Referal Program Sign

Need two graphics layouts for banners to get printed one 20x20 and another 26x26 about our referral program. WE LOVE REFERRALS " Do you have friends and family that could use our services? Refer them to us and when they open a new agreement, you pick an agreement on your account for a two-week credit!

```html
<!DOCTYPE html>
<html lang="en">
<head>
<meta charset="utf-8">
<title>We Love Referrals – Crest Furniture</title>
<link rel="stylesheet" href="https://fonts.googleapis.com/css2?family=Oswald:wght@200;700&family=Poppins:wght@400;600&display=swap">
<style>
  :root {
    --page-bg: #ededed;
    --card-bg: #ffffff;
    --brand-green: #47b04b;
    --brand-blue: #1d5fa3;
    --brand-orange: #f08a36;
    --ink: #141414;
    --white: #ffffff;
  }
  html, body {
    margin: 0;
    padding: 0;
    width: 1200px;
    height: 1158px;
    overflow: hidden;
    background: var(--page-bg);
  }
  .referral-sign {
    position: absolute;
    left: 50px;
    top: 29px;
    width: 1100px;
    height: 1100px;
    background: var(--card-bg);
  }
  .referral-sign svg {
    display: block;
    width: 100%;
    height: 100%;
  }
  .headline-thin {
    font-family: "Oswald", sans-serif;
    font-weight: 200;
    fill: var(--brand-blue);
  }
  .headline-bold {
    font-family: "Oswald", sans-serif;
    font-weight: 700;
    fill: var(--brand-green);
  }
  .brand-name {
    font-family: "Poppins", sans-serif;
    font-weight: 600;
    fill: var(--brand-blue);
  }
  .panel-question {
    font-family: "Poppins", sans-serif;
    font-weight: 600;
    fill: var(--white);
  }
  .panel-body {
    font-family: "Poppins", sans-serif;
    font-weight: 400;
    fill: var(--white);
  }
  .web-address {
    font-family: "Poppins", sans-serif;
    font-weight: 600;
    fill: var(--ink);
    letter-spacing: 1px;
  }
</style>
</head>
<body>
<main class="referral-sign">
  <svg viewBox="0 0 626 626" xmlns="http://www.w3.org/2000/svg">
    <defs>
      <linearGradient id="corner-gradient" x1="0" y1="0" x2="1" y2="0">
        <stop offset="0" stop-color="#45ad4f"/>
        <stop offset="1" stop-color="#1c5fa6"/>
      </linearGradient>
    </defs>

    <!-- corner shapes -->
    <path class="corner-shape-left" fill="url(#corner-gradient)"
          d="M13,13 H172 Q215,13 213,62 Q210,80 196,100 L42,296 Q30,310 13,305 Z"/>
    <path class="corner-shape-right" fill="var(--brand-orange)"
          d="M345,13 H613 V42 L470,190 Q445,212 420,196 Q342,140 334,42 Q333,13 345,13 Z"/>

    <!-- diagonal headline -->
    <text class="headline-thin" x="190" y="235" font-size="64"
          text-anchor="middle" dominant-baseline="central"
          textLength="396" lengthAdjust="spacingAndGlyphs"
          transform="rotate(-44 190 235)">WE LOVE</text>
    <text class="headline-bold" x="236" y="360" font-size="92"
          text-anchor="middle" dominant-baseline="central"
          textLength="484" lengthAdjust="spacingAndGlyphs"
          transform="rotate(-46 236 360)">REFERRALS</text>

    <!-- brand name -->
    <g class="brand">
      <circle cx="448" cy="345" r="15" fill="var(--brand-orange)"/>
      <text class="brand-name" x="472" y="341" font-size="22">CREST</text>
      <text class="brand-name" x="473" y="362" font-size="11" letter-spacing="3">FURNITURE</text>
    </g>

    <!-- info panel -->
    <path class="info-panel" fill="var(--brand-blue)"
          d="M318,405 H613 V613 H292 Q240,613 237,565 V485 Q237,405 318,405 Z"/>
    <text class="panel-question" font-size="17.5" text-anchor="end">
      <tspan x="595" y="446">DO YOU HAVE</tspan>
      <tspan x="595" y="473">FRIENDS AND FAMILY THAT</tspan>
      <tspan x="595" y="501">COULD USE OUR SERVICES?</tspan>
    </text>
    <text class="panel-body" font-size="12.5" text-anchor="end">
      <tspan x="595" y="533">Refer them to us and when they</tspan>
      <tspan x="595" y="552">open a new agreement, you pick an</tspan>
      <tspan x="595" y="571">agreement on your account for a</tspan>
      <tspan x="595" y="590">two-week credit!</tspan>
    </text>

    <!-- web address -->
    <text class="web-address" x="30" y="604" font-size="15">www.crestfurniture.com</text>
  </svg>
</main>
</body>
</html>
```